Postcard Design Project

script called Lanterns Over Quiet Harbor Road based on a true story and a book by the same author. It needs to have the Marlowe Creek Cinema Showcase logo and my contact info. dorothea.quillan@pellimoremail.org and phone: 555-014-7291, the logline and the synopsis on the back of the card. Below my photo: Dorothea Quillan is a script writer with shares in two Harcastle Medals, a published book, a Pellimore and other awards. Should have a large headline over the booking photo: Lanterns Over Quiet Harbor Road, feature film/drama based on a true story
Updates

I don't see where you added my web site. It should be on the front by the phone. www.dorotheaquillan.com

Target Market(s)

producers and agents looking for scripts

Industry/Entity Type

Movie Production

Font styles to use
Serif

Requirements
Must have
• www.dorotheaquillan.com dorothea.quillan@pellimoremail.org
• logline (included in the file attached), photo of the boy, author biographical infor., contact information and web site. Marlowe creek Cinema Showcase logo can be downloaded from http://marlowecreekshowcase.com/entry-rules/ I need the logo that says "official selection" at the top
Nice to have
• head shot of the author, dorothea quillan

```html
<!DOCTYPE html>
<html lang="en">
<head>
<meta charset="utf-8">
<title>Lanterns Over Quiet Harbor Road – Postcard</title>
<link rel="stylesheet" href="https://fonts.googleapis.com/css2?family=Montserrat:wght@700;800&family=Open+Sans:wght@400;600;700&display=swap">
<style>
  :root {
    --bg-top: #7d8c8e;
    --bg-mid: #5f6f72;
    --bg-low: #4f5f63;
    --gold-light: #f1dfa0;
    --gold: #d4b767;
    --gold-dark: #a98a3e;
    --band-grey: rgba(190, 198, 200, 0.55);
    --panel-teal: #2e4147;
    --footer-slate: #4b5a62;
    --ink-dark: #1f2b2f;
    --text-light: #ffffff;
    --text-soft: #dfe5e7;
    --card-paper: #d9c6a4;
    --card-photo: #6b6b68;
    --headshot: #b58a64;
  }
  html, body {
    margin: 0;
    padding: 0;
    width: 1200px;
    height: 2695px;
    overflow: hidden;
  }
  .postcard {
    position: relative;
    width: 1200px;
    height: 2695px;
    overflow: hidden;
    background: radial-gradient(ellipse at 45% 35%, var(--bg-top) 0%, var(--bg-mid) 55%, var(--bg-low) 100%);
    font-family: "Open Sans", Arial, sans-serif;
  }

  /* Festival name block */
  .festival-name {
    position: absolute;
    left: 48px;
    top: 40px;
    display: flex;
    align-items: center;
    gap: 18px;
    color: var(--text-light);
    font-family: "Open Sans", Arial, sans-serif;
    font-weight: 700;
    font-size: 44px;
    line-height: 1.05;
    width: 380px;
  }
  .festival-name .mark {
    flex: 0 0 auto;
    width: 34px;
    height: 34px;
    border-radius: 50%;
    background: var(--gold);
  }

  .selection-bar {
    position: absolute;
    left: 424px;
    top: 147px;
    width: 776px;
    height: 76px;
    background: linear-gradient(90deg, var(--gold-light) 0%, var(--gold) 45%, var(--gold-dark) 100%);
    display: flex;
    align-items: center;
    padding-left: 48px;
    box-sizing: border-box;
    font-weight: 700;
    font-size: 40px;
    color: var(--ink-dark);
  }

  /* Headline */
  .headline {
    position: absolute;
    left: 90px;
    top: 340px;
    margin: 0;
    width: 1120px;
    font-family: "Montserrat", Arial, sans-serif;
    font-weight: 800;
    font-size: 128px;
    line-height: 1.08;
    color: var(--text-light);
    text-shadow: 0 6px 10px rgba(0,0,0,0.35);
    transform: rotate(-8deg);
    transform-origin: left top;
  }
  .headline span { display: block; }
  .headline .indent { padding-left: 20px; }

  .tagline-band {
    position: absolute;
    left: -60px;
    top: 860px;
    width: 1340px;
    height: 118px;
    background: var(--band-grey);
    transform: rotate(-8deg);
    transform-origin: left top;
    display: flex;
    align-items: center;
    padding-left: 215px;
    box-sizing: border-box;
    font-family: "Montserrat", Arial, sans-serif;
    font-weight: 700;
    font-size: 49px;
    color: #44525a;
  }

  /* Booking card */
  .booking-card {
    position: absolute;
    left: 40px;
    top: 1030px;
    width: 1090px;
    height: 760px;
    background: var(--card-paper);
    transform: rotate(-7deg);
    transform-origin: center;
    box-shadow: 0 18px 30px rgba(0,0,0,0.35);
  }
  .booking-card .photo {
    position: absolute;
    left: 110px;
    top: 120px;
    width: 880px;
    height: 520px;
    background: linear-gradient(90deg, #8d8d88 0%, var(--card-photo) 50%, #8a8a85 100%);
  }

  /* Author */
  .author-band {
    position: absolute;
    left: 0;
    top: 2062px;
    width: 1200px;
    height: 88px;
    background: linear-gradient(90deg, var(--gold-dark) 0%, var(--gold-light) 40%, var(--gold) 70%, var(--gold-dark) 100%);
  }
  .author-name {
    position: absolute;
    left: 517px;
    top: 2068px;
    margin: 0;
    font-weight: 400;
    font-size: 56px;
    color: var(--ink-dark);
  }
  .author-bio {
    position: absolute;
    left: 0;
    top: 2150px;
    width: 1200px;
    height: 272px;
    background: var(--panel-teal);
    box-sizing: border-box;
    padding: 32px 16px 0 517px;
    margin: 0;
    font-size: 32px;
    line-height: 54px;
    white-space: nowrap;
    color: var(--text-light);
  }
  .headshot {
    position: absolute;
    left: 41px;
    top: 1883px;
    width: 438px;
    height: 438px;
    border-radius: 50%;
    border: 10px solid var(--gold);
    box-sizing: border-box;
    background: radial-gradient(circle at 50% 45%, #d9ab85 0%, var(--headshot) 55%, #6f4a30 100%);
    box-shadow: 0 8px 20px rgba(0,0,0,0.35);
  }

  /* Contact */
  .contact {
    position: absolute;
    left: 0;
    top: 2422px;
    width: 1200px;
    height: 273px;
    background: var(--footer-slate);
    text-align: center;
    color: var(--text-soft);
    font-size: 44px;
  }
  .contact p { margin: 0; }
  .contact .phone { padding-top: 8px; line-height: 76px; }
  .contact .email { line-height: 70px; }
  .contact .website {
    line-height: 88px;
    font-weight: 700;
    font-size: 58px;
    color: var(--text-light);
  }
</style>
</head>
<body>
<main class="postcard">
  <div class="festival-name"><span class="mark"></span><span>Marlowe Creek Cinema Showcase</span></div>
  <div class="selection-bar">Official Selection</div>

  <h1 class="headline"><span>Lanterns</span><span>Over Quiet</span><span class="indent">Harbor Road</span></h1>
  <div class="tagline-band">Feature film/drama based on a true story</div>

  <div class="booking-card" role="img" aria-label="Vintage booking photo card of a young boy, side and front views">
    <div class="photo"></div>
  </div>

  <div class="author-band"></div>
  <h2 class="author-name">Dorothea Quillan</h2>
  <p class="author-bio">Dorothea Quillan is a script writer<br>with shares in two Harcastle Medals,<br>a published book,<br>a Pellimore and other awards.</p>
  <div class="headshot" role="img" aria-label="Head shot of author Dorothea Quillan"></div>

  <footer class="contact">
    <p class="phone">555-014-7291</p>
    <p class="email">dorothea.quillan@pellimoremail.org</p>
    <p class="website">www.dorotheaquillan.com</p>
  </footer>
</main>
</body>
</html>
```